TFP Tarlo Fluid Power company brochure

We need the design of brochure of a company that provides consultancy, design and supply of key equipment in the field of Wastewater, clean water, organic waste anaerobic treatment and green energy production for Industries. The attached files are:
TFP wording in english that describes activities
Some drawings (useful for design)
Presentation (in italian)
It would be nice to have a 4 pages brochure possibly in double language (english and italian).

Target Market(s)

water and waste

Industry/Entity Type

It Company

Colors

Designer to choose colors to be used in the design.

Requirements
Must have
• use the logo TFP as per attached docs

```html
<!DOCTYPE html>
<html lang="en">
<head>
<meta charset="utf-8">
<title>TFP Tarlo Fluid Power – Brochure</title>
<link rel="stylesheet" href="https://fonts.googleapis.com/css2?family=Open+Sans:wght@400;600;700;800&display=swap">
<style>
:root{
  --bg:#a7a7a7;
  --paper:#ffffff;
  --green:#3d9a2b;
  --teal:#2b8a6a;
  --blue:#1b5f94;
  --ink:#3b3b3b;
  --muted:#6a6a6a;
  --photo-fill:#c8b88f;
  --drawing:#eceef0;
}
*{box-sizing:border-box;margin:0;padding:0}
html,body{width:1035px;height:1200px;overflow:hidden}
body{background:var(--bg);font-family:"Open Sans",Arial,sans-serif;color:var(--ink);position:relative}
.spread{position:absolute;left:70px;width:820px;height:560px;display:flex;box-shadow:0 6px 18px rgba(0,0,0,.25)}
.spread--outside{top:28px}
.spread--inside{top:616px}
.view-label{position:absolute;font-size:34px;font-weight:400;color:#fff;transform:rotate(-90deg);transform-origin:right top;letter-spacing:1px}
.view-label--outside{top:470px;right:60px}
.view-label--inside{top:1060px;right:60px}
.page{position:relative;width:410px;height:560px;background:var(--paper);overflow:hidden}
.page + .page{border-left:1px solid #ddd}
.gradient{position:absolute;inset:0;background:linear-gradient(to bottom,var(--green) 0%,var(--teal) 50%,var(--blue) 100%)}
.back .gradient{clip-path:polygon(56% 0,100% 0,100% 100%,82% 100%)}
.cover .gradient{clip-path:polygon(0 0,14% 0,20% 100%,0 100%)}
.inside-left .gradient{clip-path:polygon(68% 0,100% 0,100% 100%)}
.inside-right .gradient{clip-path:polygon(0 0,22% 0,0 92%)}
.tab{display:inline-block;background:var(--green);color:#fff;font-weight:700;font-size:10px;padding:3px 12px 3px 8px;border-radius:0 10px 10px 0;letter-spacing:.3px}
.tab--blue{background:var(--blue)}
.panel{position:absolute;background:var(--paper)}
.bullets{list-style:none;font-size:7.4px;line-height:1.35;color:var(--muted)}
.bullets > li{position:relative;padding-left:12px;margin-bottom:5px}
.bullets > li::before{content:"";position:absolute;left:1px;top:3px;width:5px;height:6px;background:var(--blue);border-radius:50%/60% 60% 40% 40%}
.checks{list-style:none;font-size:7.4px;line-height:1.3;color:var(--muted)}
.checks > li{position:relative;padding-left:13px;margin-bottom:2px}
.checks > li::before{content:"";position:absolute;left:0;top:2px;width:6px;height:6px;border:1px solid var(--blue);background:none;border-radius:0}
.checks > li::after{content:"";position:absolute;left:2px;top:2px;width:5px;height:2px;border-left:1px solid var(--green);border-bottom:1px solid var(--green);transform:rotate(-45deg)}
.checks--sub{margin-left:10px}
strong{color:var(--ink)}
.brand{display:flex;align-items:center;gap:6px;font-weight:800;color:var(--blue);font-size:15px;line-height:1}
.brand-dot{width:14px;height:14px;background:var(--green)}
.brand-name{display:flex;flex-direction:column}
.brand-name small{font-size:9px;font-weight:800}
.section-title{font-size:12px;color:var(--blue);font-weight:700;letter-spacing:.2px}
.section-title span{font-weight:400}
.contact{list-style:none;font-size:7.5px;font-weight:700;color:var(--ink);line-height:1.6}
.contact li{display:flex;align-items:center;gap:5px}
.contact svg{width:8px;height:8px;fill:var(--blue)}
.placeholder{position:absolute}
.photo{background:var(--photo-fill)}
.drawing{background:var(--drawing)}
.bottom-band{position:absolute;left:0;right:0;bottom:0;height:7px;background:var(--blue)}
.rule{height:1px;border-top:1px dashed #b9d6a8;margin:6px 0}
.numbered{list-style:none;font-size:8.5px;font-weight:700;color:var(--blue)}
.numbered > li{margin:6px 0 3px}
</style>
</head>
<body>

<section class="spread spread--outside">
  <article class="page back">
    <div class="gradient"></div>
    <div class="panel" style="left:22px;top:78px;width:250px;height:430px;">
      <div style="margin-left:-22px"><span class="tab" style="padding-left:22px">WHY TO CHOOSE US ?</span></div>
      <ul class="bullets" style="margin-top:12px;padding-right:14px">
        <li><strong>COST REDUCTION :</strong> TFP first identifies the inefficient processes and removes them.</li>
        <li>Only when the emission reduction is not any more possible or economically feasible, TFP proposes the best treatment to the client.</li>
        <li>TFP provides best solutions on a variety of biological and chemical processes.</li>
        <li>TFP provides highly qualified and independent consultancy.</li>
      </ul>
      <h3 class="section-title" style="margin-top:18px">ANAEROBIC <span>TREATMENT :</span></h3>
      <p style="font-size:8.5px;color:var(--muted);margin:3px 0 8px">Digestione anaerobica:</p>
      <ul class="checks" style="font-size:8px;line-height:1.6">
        <li>Fanghi</li>
        <li>Forsu</li>
        <li>Scarti di macellazione</li>
      </ul>
      <div class="brand" style="position:absolute;left:118px;bottom:70px">
        <span class="brand-dot"></span>
        <span class="brand-name">TFP<small>Tarlo Fluid Power</small></span>
      </div>
      <ul class="contact" style="position:absolute;left:14px;bottom:4px">
        <li><svg viewBox="0 0 10 10"><path d="M5 1 1 5h1.5v4h5V5H9z"/></svg>Via dei Tigli 28 – Novara</li>
        <li><svg viewBox="0 0 10 10"><rect x="1" y="3" width="8" height="5" rx="1"/><rect x="3" y="1" width="4" height="2"/></svg>0321.555018</li>
        <li><svg viewBox="0 0 10 10"><rect x="3" y="0.5" width="4" height="9" rx="1"/></svg>340 555 0192</li>
        <li style="padding-left:13px">PIVA: 09876543210</li>
      </ul>
    </div>
  </article>

  <article class="page cover">
    <div class="gradient"></div>
    <div class="brand" style="position:absolute;left:130px;top:40px;z-index:2">
      <span class="brand-dot"></span>
      <span class="brand-name" style="font-size:20px">TFP<small style="font-size:11px">Tarlo Fluid Power</small></span>
    </div>
    <div class="placeholder photo" role="img" aria-label="Photograph of a large anaerobic digester tank with walkways and railings" style="left:68px;top:100px;right:0;height:200px"></div>
    <div style="position:absolute;left:74px;right:0;top:300px;height:3px;background:var(--blue)"></div>
    <div style="position:absolute;left:90px;right:24px;top:318px;text-align:right">
      <p style="font-size:19px;font-weight:800;color:var(--blue)">WE VERIFY</p>
      <p style="font-size:15px;font-weight:700;color:var(--green)">any proposed process</p>
      <p style="font-size:12.5px;color:var(--blue)">with its internal labs and pilot tests</p>
      <p style="font-size:7.2px;color:var(--muted);margin-top:10px;line-height:1.45">TFP ltd (TFP) has the mission to solve any client's environmental problem with best process solution available on the market, most reliable and economical both on the CAPEX and OPEX.</p>
      <p style="font-size:7.2px;color:var(--muted);margin-top:6px;line-height:1.45">TFP wants to optimize the client's benefits: energy, water recycle, products recovery and emission minimization.</p>
    </div>
    <div style="position:absolute;left:120px;right:20px;bottom:44px;height:1px;background:var(--blue)"></div>
    <p style="position:absolute;right:30px;bottom:26px;font-size:7.5px;letter-spacing:3px;color:var(--ink)">www.tarlofluid.example</p>
  </article>
</section>

<section class="spread spread--inside">
  <article class="page inside-left">
    <div class="gradient"></div>
    <div class="panel" style="left:0;top:34px;width:290px;height:510px;padding-left:20px">
      <div style="margin-left:-20px"><span class="tab tab--blue" style="padding-left:20px">Our COMPANY :</span></div>
      <p style="font-size:7.6px;color:var(--ink);margin:5px 0 3px">At TFP nasce:</p>
      <ul class="bullets">
        <li>from the company Venturi Serbatoi Srl, for over 40 years in the treatment of industrial and liquid waste</li>
        <li>from the skills and expertise of their partners</li>
        <li>Esperienza da oltre 40 anni nella gestione di processi:
          <ul class="checks" style="margin-top:2px">
            <li>Biologici aerobici e anaerobici</li>
            <li>Chimico/fisici</li>
            <li>Rimozione metalli</li>
            <li>Riduzione cromati</li>
            <li>Ossidazione fenton</li>
          </ul>
        </li>
        <li>I partners hanno progettato, costruito e gestito oltre 250 impianti aerobici e/o anaerobici</li>
        <li>Laboratorio analitico attrezzato e disponibilità di prove pilota</li>
      </ul>
      <div style="margin:8px 0 6px -20px"><span class="tab tab--blue" style="padding-left:20px">Strengths of TFP</span></div>
      <ul class="checks" style="padding-right:10px">
        <li>Attention to the Client with selection of the best available treatment without exception - to optimize efficiency and management and investment costs.</li>
        <li>High technological level in its treatment sections, with the possibility of combining them</li>
        <li>Provide the client with maximum operating flexibility over a wide range of operating conditions and minimize management costs.</li>
        <li>Robustness of the process, thanks to the quality of the materials and the electro-instrumental equipment installed.</li>
        <li>Reliability of the technological solution, with installation of backup units where necessary.</li>
      </ul>
      <div class="placeholder drawing" role="img" aria-label="Technical line drawing of two cylindrical anaerobic digesters with a labelled anaerobic digestion section" style="left:20px;right:10px;bottom:10px;height:105px"></div>
    </div>
    <div class="bottom-band"></div>
  </article>

  <article class="page inside-right">
    <div class="gradient"></div>
    <div class="panel" style="left:60px;top:22px;right:0;height:410px;padding-right:20px">
      <span class="tab" style="border-radius:10px">TFP provides:</span>
      <ul class="checks" style="margin-top:5px">
        <li>Feasibility studies <span style="margin-left:50px">Pilot test</span></li>
        <li>Process design and guarantees (over 240 plants successfully executed and running)</li>
        <li>Basic and detailed engineering</li>
        <li>Key equipment support</li>
        <li>Construction and start-up supervision</li>
        <li>Operation and supervision expertise (more than 20 years of internal expertise of various biological and chemical reactions)</li>
      </ul>
      <div class="rule"></div>
      <span class="tab" style="border-radius:10px">Proposed technologies:</span>
      <ol class="numbered">
        <li>1. &nbsp;Biological processes:
          <ul class="checks checks--sub" style="font-weight:400">
            <li>Oxidation, nitrification, denitrification, P-removal</li>
            <li>N-recovery and slow release fertilizers production</li>
            <li>Anaerobic processes</li>
            <li>Metal recovery</li>
          </ul>
        </li>
        <li>2. &nbsp;High value products recovery</li>
        <li>3. &nbsp;Chemico/Phisical processes:
          <ul class="checks checks--sub" style="font-weight:400">
            <li>Flottation</li>
            <li>Filtration and membrane filtration</li>
            <li>Chemical oxidations / reductions (e.g. Fenton, colour removal, CN, Cr6+ removal ….)</li>
            <li>Disinfection</li>
          </ul>
        </li>
        <li>4. &nbsp;Water recovery and recycle</li>
      </ol>
    </div>
    <div class="placeholder drawing" role="img" aria-label="Technical line drawing of a treatment plant building with storage tanks" style="left:130px;right:14px;bottom:24px;height:90px"></div>
    <div class="bottom-band"></div>
  </article>
</section>

<span class="view-label view-label--outside">Outside</span>
<span class="view-label view-label--inside">Inside</span>

</body>
</html>
```